Poster for a new "Pizza Roll" Combo at our bakery

We are a cinnamon roll and coffee focused bakery, but we would like an innovative poster design to bring attention to our new offering, a Pizza Roll. We will be offering it as a combo, and this is what we wish to advertise. It will be geared mainly towards a younger high school aged crowd. I have included pics of the Pizza Rolls, but it's up to you how you want to incorporate them in the design.Poster should include our logo, the pizza rolls, and can include a drink to illustrate the combo as well. ( we offer710 ml vima bottle products and lurn bottled waters)Main Text: Try our amazing new Pizza Rolls! Message to get accross: $6.00 for a Pizza Roll and drink.Small Print: Avail after 11am, while supplies last. Includes one pizza roll and one bottled drink of choice. Taxes extra.

Target Market(s)

Broad, but mainly high school aged kids

Industry/Entity Type

Bakery

Colors

Designer to choose colors to be used in the design.

Requirements
Must have
• Text: " Try our amazing new PIzza Rolls!:
• $6 Pizza Roll Combo (Pizza Roll and a drink)
Nice to have
• Pic of the PIzza Roll (photo shopped if needed to improve esthetics)
• Pic of a Bottled 710ml vima drink
Should not have
• Any animal product references, as we are a Vegan shop.

```html
<!DOCTYPE html>
<html lang="en">
<head>
<meta charset="utf-8">
<title>Pizza Roll Combo Poster</title>
<link href="https://fonts.googleapis.com/css2?family=Lobster&family=Archivo+Black&family=Fredoka:wght@700&family=Anton&family=Kaushan+Script&display=swap" rel="stylesheet">
<style>
  :root {
    --page: #ffffff;
    --ribbon-red: #f10a12;
    --ribbon-shadow: #2a2a2a;
    --royal-blue: #0b0fe0;
    --sky-blue: #6a7bff;
    --lime: #46f20a;
    --corner-red: #f01020;
    --dash-white: #ffffff;
    --ink: #111111;
    --try-red: #ee1820;
    --roll-yellow: #ffef12;
    --coupon-yellow: #fbe81a;
    --coupon-orange: #f18a12;
    --price-red: #e8141c;
    --dot-blue: #1010e0;
  }
  html, body {
    margin: 0;
    width: 1200px;
    height: 1200px;
    overflow: hidden;
    background: var(--page);
  }
  .poster {
    position: absolute;
    left: 236px;
    top: 62px;
    width: 748px;
    height: 1096px;
    overflow: hidden;
  }
  .poster-art {
    position: absolute;
    inset: 0;
    width: 748px;
    height: 1096px;
  }
  .headline {
    position: absolute;
    margin: 0;
    font-family: "Lobster", cursive;
    font-weight: 400;
    color: #fff;
    -webkit-text-stroke: 2px var(--ink);
    text-shadow: 2px 2px 0 var(--ink);
    line-height: 1;
    text-align: center;
  }
  .headline-our { left: 260px; top: 32px; width: 120px; font-size: 56px; }
  .headline-new { left: 120px; top: 112px; width: 480px; font-size: 64px; transform: rotate(2deg); }
  .try {
    position: absolute;
    left: 430px; top: 585px; width: 160px;
    margin: 0;
    font-family: "Kaushan Script", cursive;
    font-size: 82px;
    color: var(--try-red);
    -webkit-text-stroke: 1.5px #fff;
    text-align: center;
    line-height: 1;
  }
  .amazing {
    position: absolute;
    left: 290px; top: 684px; width: 420px;
    margin: 0;
    font-family: "Archivo Black", sans-serif;
    font-size: 40px;
    color: var(--ink);
    -webkit-text-stroke: 1.5px #fff;
    text-align: center;
    line-height: 1;
    word-spacing: 8px;
  }
  .pizza-rolls {
    position: absolute;
    left: 350px; top: 740px; width: 400px;
    margin: 0;
    font-family: "Fredoka", sans-serif;
    font-weight: 700;
    font-size: 56px;
    color: var(--roll-yellow);
    text-align: center;
    line-height: 1;
    transform: rotate(-3deg) skewX(-8deg);
  }
  .coupon-price {
    position: absolute;
    left: 78px; top: 862px;
    margin: 0;
    font-family: "Archivo Black", sans-serif;
    font-size: 50px;
    color: var(--price-red);
    -webkit-text-stroke: 1.5px #7a0a0a;
    line-height: 1;
  }
  .coupon-title {
    position: absolute;
    left: 104px; top: 938px;
    margin: 0;
    font-family: "Anton", sans-serif;
    font-size: 24px;
    line-height: 33px;
    color: var(--ink);
    -webkit-text-stroke: 0.6px #fff;
  }
  .coupon-fine {
    position: absolute;
    left: 64px; top: 1002px; width: 308px;
    margin: 0;
    font-family: Georgia, serif;
    font-style: italic;
    color: var(--ink);
    text-align: center;
    line-height: 13px;
  }
  .coupon-fine .fine-main { font-size: 10.5px; display: block; padding-left: 40px; }
  .coupon-fine .fine-sub { font-size: 8.2px; display: block; white-space: nowrap; }
</style>
</head>
<body>
<main class="poster">
  <svg class="poster-art" viewBox="295 78 935 1369" preserveAspectRatio="none" xmlns="http://www.w3.org/2000/svg">
    <defs>
      <linearGradient id="rollPhotoTone" x1="0" y1="0" x2="1" y2="1">
        <stop offset="0" stop-color="#f3d9b0"/>
        <stop offset="0.35" stop-color="#e08a3c"/>
        <stop offset="0.6" stop-color="#f0c58e"/>
        <stop offset="1" stop-color="#d9772e"/>
      </linearGradient>
      <linearGradient id="cornerRed" x1="0" y1="0" x2="1" y2="0">
        <stop offset="0" stop-color="#6a1fd8"/>
        <stop offset="0.35" stop-color="var(--corner-red)"/>
        <stop offset="1" stop-color="var(--corner-red)"/>
      </linearGradient>
      <linearGradient id="couponFill" x1="0" y1="0" x2="1" y2="0.4">
        <stop offset="0" stop-color="var(--coupon-yellow)"/>
        <stop offset="0.55" stop-color="#fff02a"/>
        <stop offset="1" stop-color="var(--coupon-orange)"/>
      </linearGradient>
      <radialGradient id="comboPhotoTone" cx="0.5" cy="0.5" r="0.6">
        <stop offset="0" stop-color="#9a9cb8"/>
        <stop offset="0.7" stop-color="#6b6e8a"/>
        <stop offset="1" stop-color="#c9cad6"/>
      </radialGradient>
    </defs>

    <!-- food photo area -->
    <rect x="295" y="280" width="935" height="900" fill="url(#rollPhotoTone)" role="img" aria-label="Close-up photo of baked pizza rolls with swirls of tomato sauce"/>

    <!-- top-right blue panel -->
    <path d="M800,78 H1230 V328 Q1150,312 1070,298 V78 Z" fill="var(--royal-blue)"/>
    <path d="M1070,298 Q1150,312 1230,322" fill="none" stroke="var(--sky-blue)" stroke-width="10"/>

    <!-- lower blue wave -->
    <path d="M460,1052 C600,900 760,790 1000,776 Q1150,770 1230,790 V1447 H460 Z" fill="var(--royal-blue)"/>
    <path d="M460,1052 C600,900 760,790 1000,776 Q1150,770 1230,790" fill="none" stroke="var(--sky-blue)" stroke-width="16"/>

    <!-- green corner -->
    <path d="M295,920 L880,1447 H295 Z" fill="var(--lime)"/>
    <!-- red corner -->
    <path d="M1230,1150 V1447 H880 Z" fill="url(#cornerRed)"/>

    <!-- dashed frame -->
    <rect x="318" y="100" width="892" height="1328" fill="none" stroke="var(--dash-white)" stroke-width="7" stroke-dasharray="30 14"/>

    <!-- title ribbon -->
    <path d="M295,84 H1056 Q1081,91 1074,136 Q1036,196 1064,256 Q1081,316 1066,351 Q1061,368 1041,368 H295 Z" fill="var(--ribbon-shadow)"/>
    <path d="M295,78 H1050 Q1075,85 1068,130 Q1030,190 1058,250 Q1075,310 1060,345 Q1055,362 1035,362 H295 Z" fill="var(--ribbon-red)"/>
    <path d="M307,94 H1040 Q1058,104 1052,138 Q1016,194 1043,254 Q1058,306 1044,336 Q1040,346 1028,346 H307" fill="none" stroke="var(--dash-white)" stroke-width="3.5" stroke-dasharray="10 6"/>

    <!-- combo photo in torn hole -->
    <path d="M790,1150 L835,1100 L880,1112 L905,1085 L960,1108 L1010,1098 L1060,1115 L1100,1150 L1122,1185 L1098,1230 L1115,1290 L1075,1320 L1040,1362 L980,1350 L925,1365 L880,1345 L825,1320 L808,1280 L780,1240 L795,1200 Z" fill="url(#comboPhotoTone)" stroke="#e9e9ef" stroke-width="10" stroke-linejoin="round" role="img" aria-label="Plate of pizza rolls beside a bottled soft drink, shown through torn paper"/>

    <!-- coupon -->
    <rect x="358" y="1162" width="404" height="240" rx="32" fill="none" stroke="var(--dash-white)" stroke-width="7" stroke-dasharray="24 12"/>
    <rect x="370" y="1175" width="380" height="214" rx="22" fill="url(#couponFill)" stroke="#fff" stroke-width="2"/>
    <g fill="var(--dot-blue)">
      <circle cx="734" cy="1278" r="6.5"/><circle cx="734" cy="1299" r="6.5"/><circle cx="734" cy="1320" r="6.5"/><circle cx="734" cy="1342" r="6.5"/><circle cx="734" cy="1363" r="6.5"/>
      <circle cx="489" cy="1378" r="6.5"/><circle cx="510" cy="1378" r="6.5"/><circle cx="531" cy="1378" r="6.5"/><circle cx="552" cy="1378" r="6.5"/><circle cx="573" cy="1378" r="6.5"/><circle cx="594" cy="1378" r="6.5"/><circle cx="615" cy="1378" r="6.5"/><circle cx="636" cy="1378" r="6.5"/><circle cx="657" cy="1378" r="6.5"/><circle cx="678" cy="1378" r="6.5"/><circle cx="699" cy="1378" r="6.5"/><circle cx="720" cy="1378" r="6.5"/>
    </g>
  </svg>

  <h1 class="headline headline-our">Our</h1>
  <p class="headline headline-new">New offering</p>

  <p class="try">Try</p>
  <p class="amazing">Our amazing new</p>
  <p class="pizza-rolls">Pizza Rolls!</p>

  <p class="coupon-price">$6</p>
  <p class="coupon-title">Pizza Roll Combo<br>(Pizza Roll and a drink)</p>
  <p class="coupon-fine">
    <span class="fine-main">Avail after 11am, while supplies last.</span>
    <span class="fine-sub">Includes one pizza roll and one bottled drink of choice. Taxes extra.</span>
  </p>
</main>
</body>
</html>
```